integrative health clinic-Medical massage, acupuncture, chiropractic

we like our logo, but are open to new ideas. We need a new card design. We have added chiropractic and acupuncture that we have put under the name of the business. We are an integrative medical clinic

Target Market(s)

General public, athletes

Contact Information for Business Card

Phone 5055583927
Fax 5055583926
Hours Monday-Friday 9-6
Saturday 10-6
The 20% can be smaller on the back

Colors
3176b5
0355a3

Requirements
Must have
• Logo but am open to ideas
Nice to have
• We are an integrated medical clinic but also want to be personable. We want the card fun and inviting

```html
<!DOCTYPE html>
<html lang="en">
<head>
<meta charset="utf-8">
<title>Full Circle Vitality – Business Cards</title>
<link rel="stylesheet" href="https://fonts.googleapis.com/css2?family=EB+Garamond:ital,wght@0,400;0,500;0,600;1,400&family=Work+Sans:wght@400;500&display=swap">
<style>
  :root {
    --bg: #1d1d1d;
    --card: #ffffff;
    --ink: #1e1e1e;
    --ink-soft: #3a3a3a;
    --brand-blue: #3347a9;
    --rule: #c9cde0;
  }
  * { box-sizing: border-box; margin: 0; padding: 0; }
  html, body {
    width: 1200px; height: 930px; overflow: hidden;
    background: var(--bg);
  }
  .stage { position: relative; width: 1200px; height: 930px; }

  .card {
    position: absolute;
    width: 560px; height: 320px;
    background: var(--card);
    border-radius: 22px;
    overflow: hidden;
  }

  /* Front card */
  .card--front { left: 80px; top: 90px; font-family: "EB Garamond", serif; color: var(--ink); }
  .front__book {
    position: absolute; top: 34px; left: 0; width: 100%;
    text-align: center; font-size: 22px; font-weight: 600;
  }
  .front__brand {
    position: absolute; top: 72px; left: 58px;
    display: flex; align-items: center; gap: 14px;
  }
  .front__dot { width: 30px; height: 30px; border-radius: 50%; background: var(--brand-blue); }
  .front__name { font-size: 58px; font-weight: 500; line-height: 1; color: var(--ink); }
  .front__tagline {
    position: absolute; top: 142px; left: 150px;
    font-size: 24px; font-style: italic; color: var(--ink-soft);
  }
  .front__offer {
    position: absolute; top: 194px; left: 0; width: 100%;
    text-align: center; font-size: 32px; font-weight: 500; letter-spacing: 0.5px;
  }
  .front__band {
    position: absolute; left: 0; bottom: 0; width: 100%; height: 56px;
    background: var(--brand-blue); color: #fff;
    display: flex; align-items: center; justify-content: center;
    font-size: 21px; font-style: italic;
  }

  /* Back card */
  .card--back { left: 560px; top: 510px; font-family: "Work Sans", sans-serif; }
  .back__name {
    position: absolute; top: 40px; left: 44px;
    font-size: 38px; font-weight: 500; color: var(--brand-blue); line-height: 1;
  }
  .back__services {
    position: absolute; top: 86px; left: 48px;
    font-size: 19px; color: var(--ink-soft); line-height: 1.2;
  }
  .back__services .sub { font-size: 16px; }
  .back__special {
    position: absolute; top: 158px; left: 48px;
    font-size: 15px; color: var(--ink-soft); line-height: 1.3;
  }
  .back__mark {
    position: absolute; left: 48px; bottom: 34px;
    font-size: 20px; font-weight: 500; color: var(--brand-blue);
  }
  .back__contact {
    position: absolute; top: 158px; left: 290px;
    padding-left: 14px; border-left: 1px solid var(--rule);
    list-style: none;
  }
  .back__contact li {
    display: flex; align-items: center; gap: 10px;
    font-size: 14px; color: var(--ink-soft); height: 24px;
  }
  .back__contact svg { width: 13px; height: 13px; flex: none; fill: var(--brand-blue); }
</style>
</head>
<body>
<main class="stage">

  <section class="card card--front" aria-label="Card front">
    <p class="front__book">Book Online</p>
    <div class="front__brand">
      <span class="front__dot"></span>
      <span class="front__name">Full Circle Vitality</span>
    </div>
    <p class="front__tagline">Sports Therapy and Wellness Center</p>
    <p class="front__offer">20% OFF FIRST VISIT</p>
    <p class="front__band">We accept some insurances, Worker's Comp and Personal Injury.</p>
  </section>

  <section class="card card--back" aria-label="Card back">
    <h1 class="back__name">Full Circle Vitality</h1>
    <p class="back__services">Medical and Sports Massage<br><span class="sub">chiropractic and acupuncture</span></p>
    <p class="back__special">Specializing in<br>Medical, Sports Massage<br>and Manual Therapies</p>
    <p class="back__mark">Full Circle Vitality</p>
    <ul class="back__contact">
      <li>
        <svg viewBox="0 0 24 24" aria-hidden="true"><path d="M6.6 10.8a15 15 0 0 0 6.6 6.6l2.2-2.2a1 1 0 0 1 1-.25 11.4 11.4 0 0 0 3.6.6 1 1 0 0 1 1 1V20a1 1 0 0 1-1 1A17 17 0 0 1 3 4a1 1 0 0 1 1-1h3.5a1 1 0 0 1 1 1c0 1.25.2 2.45.6 3.6a1 1 0 0 1-.25 1z"/></svg>
        (505) 558-3927
      </li>
      <li>
        <svg viewBox="0 0 24 24" aria-hidden="true"><path d="M2 5h20v14H2zm2 2v.5l8 5 8-5V7l-8 5z"/></svg>
        info@fullcirclevitality.com
      </li>
      <li>
        <svg viewBox="0 0 24 24" aria-hidden="true"><path d="M12 2a7 7 0 0 0-7 7c0 5 7 13 7 13s7-8 7-13a7 7 0 0 0-7-7zm0 9.5A2.5 2.5 0 1 1 12 6.5a2.5 2.5 0 0 1 0 5z"/></svg>
        418 Alameda Ct, B4 Santa Fe. NM 87501
      </li>
      <li>
        <svg viewBox="0 0 24 24" aria-hidden="true"><path d="M12 2a10 10 0 1 0 0 20 10 10 0 0 0 0-20zm6.9 6h-3a15 15 0 0 0-1.3-3.9A8 8 0 0 1 18.9 8zM12 4c.8 1.2 1.5 2.5 1.9 4h-3.8c.4-1.5 1.1-2.8 1.9-4zM4.3 14a8 8 0 0 1 0-4h3.4a16 16 0 0 0 0 4zm.8 2h3a15 15 0 0 0 1.3 3.9A8 8 0 0 1 5.1 16zm3-8h-3a8 8 0 0 1 4.3-3.9A15 15 0 0 0 8.1 8zM12 20c-.8-1.2-1.5-2.5-1.9-4h3.8c-.4 1.5-1.1 2.8-1.9 4zm2.3-6H9.7a14 14 0 0 1 0-4h4.6a14 14 0 0 1 0 4zm.3 5.9a15 15 0 0 0 1.3-3.9h3a8 8 0 0 1-4.3 3.9zM16.3 14a16 16 0 0 0 0-4h3.4a8 8 0 0 1 0 4z"/></svg>
        www.fullcirclevitality.com
      </li>
    </ul>
  </section>

</main>
</body>
</html>
```